Brisk Hive 360 Postcard Design, Double-Sided

Please read carefully and see attached. Designers that do not follow these instructions will not be selected. Limit ONE design submission per artist. The ONE design submission shall show both the front and the back designs. Designs must comply with the attached dismensions accounting for the bleed area to prevent designs from being cut off during printing. The attached business card and door tag designs have already been created, printed and are in use. The postcard shall be similar in design to the attached business card and door tag. All of the information that you need is attached. The overall size is 4.12" x 6.12" for the front. The back is different, see attached and scale to match template. I would like the Veteran Owned Business logo added as well. It would also be nice to see my photo incorporated somehow. I like the yellow on the door tag. It helps build contrast and pops out. Again, one design submission per designer that shows both the front and the back.

Target Market(s)

Please read all instructions and see attached.

Industry/Entity Type

Requirements
Must have
• Please read all instructions and see attached.
Nice to have
Should not have

```html
<!DOCTYPE html>
<html lang="en">
<head>
<meta charset="utf-8">
<title>Brisk Hive 360 Postcard</title>
<link rel="stylesheet" href="https://fonts.googleapis.com/css2?family=Anton&family=Montserrat:ital,wght@0,800;1,800;1,900&family=Poppins:wght@400;600&family=Arimo&display=swap">
<style>
  :root{
    --ink:#000;
    --paper:#fff;
    --lime:#d6e021;
    --stage:#a3a3a3;
    --wood-light:#e4e0d8;
    --wood-mid:#b9a58a;
    --tool-brown:#8a5a2c;
    --tool-dark:#4a3a2c;
  }
  *{box-sizing:border-box;margin:0;padding:0}
  html,body{width:1200px;height:1117px;overflow:hidden;background:var(--stage)}
  .card{position:absolute;left:240px;width:739px;height:497px;overflow:hidden;background:var(--paper)}
  .card--front{top:49px}
  .card--back{top:569px}
  .card__art{position:absolute;inset:0;width:739px;height:497px}
  .text{position:absolute;white-space:nowrap;line-height:1}

  .logo-name{left:44px;top:132px;width:200px;text-align:center;font-family:"Montserrat",sans-serif;font-weight:800;font-size:19px;color:var(--ink)}
  .brand-title{left:52px;top:266px;font-family:"Anton",sans-serif;font-size:52px;color:var(--paper);letter-spacing:-1px}
  .brand-title .accent{color:var(--lime)}
  .title-rule{position:absolute;left:52px;top:326px;width:290px;height:3px;background:var(--paper)}
  .trade{left:52px;top:338px;font-family:"Montserrat",sans-serif;font-style:italic;font-weight:900;font-size:41px;color:var(--lime)}
  .name-band{position:absolute;left:0;top:392px;width:343px;height:41px;background:var(--paper)}
  .owner-name{left:52px;top:398px;font-family:"Montserrat",sans-serif;font-style:italic;font-weight:800;font-size:27px;color:var(--ink);letter-spacing:-.5px}
  .owner-role{left:52px;top:442px;font-family:"Montserrat",sans-serif;font-style:italic;font-weight:800;font-size:18px;color:var(--lime)}
  .divider{position:absolute;width:2px;background:var(--paper)}
  .divider--front{left:379px;top:327px;height:130px}

  .contact{position:absolute;list-style:none;font-family:"Poppins",sans-serif;font-weight:600;color:var(--paper)}
  .contact li{display:flex;align-items:center;white-space:nowrap}
  .contact svg{flex:none}
  .contact--front{left:413px;top:352px;font-size:18px}
  .contact--front li{height:28px}
  .contact--front svg{width:15px;height:15px;margin-right:7px}
  .contact--back{left:424px;top:43px;font-size:10.3px;font-weight:400;letter-spacing:-.1px}
  .contact--back li{height:19px}
  .contact--back svg{width:9px;height:9px;margin-right:5px}

  .heading{font-family:"Montserrat",sans-serif;font-weight:800;color:var(--paper);line-height:.95}
  .services-title{left:48px;top:44px;font-size:22px}
  .benefits-title{left:225px;top:45px;font-size:17px}
  .checklist{position:absolute;list-style:none;font-family:"Poppins",sans-serif;color:var(--paper)}
  .checklist li{display:flex;align-items:center;white-space:nowrap}
  .checklist svg{width:10px;height:10px;margin-right:8px;flex:none}
  .checklist--services{left:48px;top:74px;font-size:11.5px}
  .checklist--services li{height:15.3px}
  .checklist--benefits{left:225px;top:102px;font-size:13px}
  .checklist--benefits li{height:20.3px}
  .checklist--benefits svg{margin-right:12px}
  .divider--services{left:202px;top:48px;height:133px;width:1.5px}
  .divider--contact{left:406px;top:32px;height:90px;width:1.5px;background:var(--lime)}

  .postage{position:absolute;left:608px;top:30px;width:100px;height:100px;border:1.5px solid var(--ink);display:flex;align-items:center;justify-content:center;font-family:"Montserrat",sans-serif;font-weight:800;font-size:12px}
  .mail-address{position:absolute;left:446px;top:277px;font-family:"Arimo",sans-serif;font-size:16px;line-height:23.5px;color:#111;font-style:normal}
</style>
</head>
<body>

<section class="card card--front">
  <svg class="card__art" viewBox="0 0 739 497">
    <defs>
      <linearGradient id="wood" x1="0" y1="0" x2="1" y2="1">
        <stop offset="0" stop-color="var(--wood-light)"/>
        <stop offset="1" stop-color="var(--wood-mid)"/>
      </linearGradient>
      <radialGradient id="tools" cx=".55" cy=".6" r=".6">
        <stop offset="0" stop-color="var(--tool-brown)"/>
        <stop offset="1" stop-color="var(--tool-dark)"/>
      </radialGradient>
    </defs>
    <rect width="739" height="497" fill="var(--ink)"/>
    <rect width="739" height="400" fill="url(#wood)" role="img" aria-label="Photo of flat-pack furniture boards on a workbench"/>
    <path d="M0,245 Q150,205 330,200 L739,385 L739,497 L0,497 Z" fill="var(--ink)"/>
    <path d="M0,237 Q150,197 330,192 L345,200 Q150,205 0,245 Z" fill="var(--lime)"/>
    <path d="M630,330 L739,372 L739,395 L650,345 Z" fill="var(--lime)"/>
    <circle cx="525" cy="30" r="305" fill="var(--paper)"/>
    <circle cx="525" cy="30" r="298" fill="var(--lime)"/>
    <circle cx="525" cy="30" r="285" fill="url(#tools)" role="img" aria-label="Photo of hammer, pliers, screwdrivers and cordless drill in a leather tool belt"/>
    <circle cx="144" cy="142" r="108" fill="var(--paper)"/>
    <circle cx="144" cy="142" r="98" fill="none" stroke="var(--ink)" stroke-width="6"/>
  </svg>

  <div class="text logo-name">Brisk Hive 360</div>
  <div class="text brand-title">BRISK HIVE <span class="accent">360</span></div>
  <div class="title-rule"></div>
  <div class="text trade">HANDYMAN</div>
  <div class="name-band"></div>
  <div class="text owner-name">DANA R.KOVAC</div>
  <div class="text owner-role">OWNER &amp; HANDYMAN</div>
  <div class="divider divider--front"></div>

  <ul class="contact contact--front">
    <li><svg viewBox="0 0 16 16"><circle cx="8" cy="8" r="8" fill="var(--lime)"/><path d="M5 4l2 2-1 1.2c.6 1.3 1.5 2.2 2.8 2.8L10 9l2 2-1.2 1.3C7.5 12 4 8.5 3.7 5.2Z" fill="var(--ink)"/></svg>(555) 014-2278</li>
    <li><svg viewBox="0 0 16 16"><path d="M8 0a5.5 5.5 0 0 0-5.5 5.5C2.5 10 8 16 8 16s5.5-6 5.5-10.5A5.5 5.5 0 0 0 8 0Z" fill="var(--lime)"/><circle cx="8" cy="5.5" r="2" fill="var(--ink)"/></svg>Palmetto Cove, florida</li>
    <li><svg viewBox="0 0 16 16"><circle cx="8" cy="8" r="8" fill="var(--lime)"/><rect x="4" y="5" width="8" height="6" fill="none" stroke="var(--ink)" stroke-width="1.2"/><path d="M4 5l4 3.2L12 5" fill="none" stroke="var(--ink)" stroke-width="1.2"/></svg>Service@BriskHive360.com</li>
    <li><svg viewBox="0 0 16 16"><circle cx="8" cy="8" r="8" fill="var(--lime)"/><circle cx="8" cy="8" r="4.5" fill="none" stroke="var(--ink)" stroke-width="1.1"/><path d="M3.5 8h9M8 3.5v9" stroke="var(--ink)" stroke-width="1.1"/></svg>BriskHive360.com</li>
  </ul>
</section>

<section class="card card--back">
  <svg class="card__art" viewBox="0 0 739 497">
    <defs>
      <linearGradient id="boards" x1="0" y1="0" x2="1" y2="1">
        <stop offset="0" stop-color="#c9a878"/>
        <stop offset="1" stop-color="#a27a4c"/>
      </linearGradient>
    </defs>
    <rect width="739" height="497" fill="var(--paper)"/>
    <path d="M0,0 H590 V138 H406 V262 Q250,170 0,242 Z" fill="var(--ink)"/>
    <path d="M0,252 Q250,182 406,272 V406 H148 V497 H0 Z" fill="url(#boards)" role="img" aria-label="Photo of white chair parts laid out for assembly on cardboard"/>
    <path d="M0,246 Q250,176 406,265" fill="none" stroke="var(--lime)" stroke-width="12"/>
    <circle class="partner-badge" cx="316" cy="337" r="58" fill="var(--paper)" role="img" aria-label="Veteran owned business membership badge"/>
  </svg>

  <div class="text heading services-title">SERVICES:</div>
  <ul class="checklist checklist--services">
    <li><svg viewBox="0 0 10 10"><path d="M1 5.5l2.5 2.5L9 2" fill="none" stroke="var(--lime)" stroke-width="2"/></svg>Assembly</li>
    <li><svg viewBox="0 0 10 10"><path d="M1 5.5l2.5 2.5L9 2" fill="none" stroke="var(--lime)" stroke-width="2"/></svg>Small Repairs</li>
    <li><svg viewBox="0 0 10 10"><path d="M1 5.5l2.5 2.5L9 2" fill="none" stroke="var(--lime)" stroke-width="2"/></svg>Wifi/Router Setup</li>
    <li><svg viewBox="0 0 10 10"><path d="M1 5.5l2.5 2.5L9 2" fill="none" stroke="var(--lime)" stroke-width="2"/></svg>Fabrication</li>
    <li><svg viewBox="0 0 10 10"><path d="M1 5.5l2.5 2.5L9 2" fill="none" stroke="var(--lime)" stroke-width="2"/></svg>Hanging Items</li>
    <li><svg viewBox="0 0 10 10"><path d="M1 5.5l2.5 2.5L9 2" fill="none" stroke="var(--lime)" stroke-width="2"/></svg>Wireless Device Setup</li>
    <li><svg viewBox="0 0 10 10"><path d="M1 5.5l2.5 2.5L9 2" fill="none" stroke="var(--lime)" stroke-width="2"/></svg>Odd Jobs</li>
  </ul>
  <div class="divider divider--services"></div>

  <div class="text heading benefits-title">BENEFITS<br>OF USING OUR<br>SERVICES</div>
  <ul class="checklist checklist--benefits">
    <li><svg viewBox="0 0 10 10"><path d="M1 5.5l2.5 2.5L9 2" fill="none" stroke="var(--lime)" stroke-width="2"/></svg>Fast Response</li>
    <li><svg viewBox="0 0 10 10"><path d="M1 5.5l2.5 2.5L9 2" fill="none" stroke="var(--lime)" stroke-width="2"/></svg>High Quality</li>
    <li><svg viewBox="0 0 10 10"><path d="M1 5.5l2.5 2.5L9 2" fill="none" stroke="var(--lime)" stroke-width="2"/></svg>Fair Pricing</li>
    <li><svg viewBox="0 0 10 10"><path d="M1 5.5l2.5 2.5L9 2" fill="none" stroke="var(--lime)" stroke-width="2"/></svg>Veteran Owned</li>
  </ul>
  <div class="divider divider--contact"></div>

  <ul class="contact contact--back">
    <li><svg viewBox="0 0 16 16"><circle cx="8" cy="8" r="8" fill="var(--lime)"/><path d="M5 4l2 2-1 1.2c.6 1.3 1.5 2.2 2.8 2.8L10 9l2 2-1.2 1.3C7.5 12 4 8.5 3.7 5.2Z" fill="var(--ink)"/></svg>(555) 014-2278</li>
    <li><svg viewBox="0 0 16 16"><path d="M8 0a5.5 5.5 0 0 0-5.5 5.5C2.5 10 8 16 8 16s5.5-6 5.5-10.5A5.5 5.5 0 0 0 8 0Z" fill="var(--lime)"/><circle cx="8" cy="5.5" r="2" fill="var(--ink)"/></svg>Palmetto Cove, florida</li>
    <li><svg viewBox="0 0 16 16"><circle cx="8" cy="8" r="8" fill="var(--lime)"/><rect x="4" y="5" width="8" height="6" fill="none" stroke="var(--ink)" stroke-width="1.2"/><path d="M4 5l4 3.2L12 5" fill="none" stroke="var(--ink)" stroke-width="1.2"/></svg>Service@BriskHive360.com</li>
    <li><svg viewBox="0 0 16 16"><circle cx="8" cy="8" r="8" fill="var(--lime)"/><circle cx="8" cy="8" r="4.5" fill="none" stroke="var(--ink)" stroke-width="1.1"/><path d="M3.5 8h9M8 3.5v9" stroke="var(--ink)" stroke-width="1.1"/></svg>BriskHive360.com</li>
  </ul>

  <div class="postage">POSTAGE</div>
  <address class="mail-address">John Smith<br>123 Main Street<br>Small Town, USA 00000-0000</address>
</section>

</body>
</html>
```